Business Card Re-Design for a Lighting Designer

I would like my business card re-designed. It is currently high gloss and they scratch too easily. I don not think the current design lends itself well to a matte finish. I have included the current design for reference along with our company logo.
Check out our website for current branding.
http://www.brenmoorastudio.example

Updates
Some of the top contenders are muslim and it is a holiday for them. I do not want to discriminate and would expect the same courtesy for holidays we celebrate.
Target Market(s)
Interior Designers, Architects
Contact Information for Business Card
Logo - Name, Title, Address, Telephone Number and Extension, Email
Font styles to use
Requirements
Must have
- All the information listed on the current business card. If you use Red, it needs to be the red from our logo.
Nice to have
- Vertical and Horizontal Designs will be entertained.
Should not have
- Requirements for a glossy finish...should not look too corporate since we are a design firm.

```html
<!DOCTYPE html>
<html lang="en">
<head>
<meta charset="utf-8">
<title>Bren Moora Studio – Business Card</title>
<link rel="stylesheet" href="https://fonts.googleapis.com/css2?family=Lato:wght@400;700&family=Oswald:wght@400;500&display=swap">
<style>
  :root {
    --brand-red: #990000;
    --paper: #ffffff;
    --backdrop: #a0a0a0;
    --ink: #2b2b2b;
    --rule: #bdbdbd;
  }
  * { margin: 0; padding: 0; box-sizing: border-box; }
  html, body { width: 1200px; height: 900px; overflow: hidden; }
  body {
    background: var(--backdrop);
    position: relative;
    font-family: "Lato", Arial, sans-serif;
    color: var(--ink);
  }
  .card {
    position: absolute;
    top: 200px;
    width: 310px;
    height: 502px;
  }
  .card--front {
    left: 253px;
    background: var(--paper);
    border-radius: 56px 0 60px 0;
  }
  .card--back {
    left: 627px;
    background: var(--brand-red);
    border-radius: 0 56px 0 60px;
  }
  .wordmark {
    position: absolute;
    left: 0; right: 0;
    display: flex;
    align-items: center;
    justify-content: center;
    gap: 12px;
  }
  .card--front .wordmark { top: 120px; color: var(--brand-red); }
  .card--back .wordmark { top: 212px; color: var(--paper); }
  .wordmark__square {
    width: 40px; height: 40px;
    background: currentColor;
    flex: none;
  }
  .wordmark__name {
    font-family: "Lato", Arial, sans-serif;
    font-weight: 400;
    font-size: 27px;
    line-height: 1.05;
    text-transform: uppercase;
    letter-spacing: 0.5px;
  }
  .contact {
    position: absolute;
    left: 34px;
    top: 284px;
    width: 230px;
  }
  .contact__name {
    font-family: "Oswald", "Arial Narrow", sans-serif;
    font-weight: 400;
    font-size: 22px;
    line-height: 26px;
    color: var(--brand-red);
    text-transform: uppercase;
  }
  .contact__title {
    font-size: 15px;
    line-height: 18px;
    padding-bottom: 10px;
    border-bottom: 1px solid var(--rule);
  }
  .contact__list {
    list-style: none;
    padding: 8px 0 8px;
    border-bottom: 1px solid var(--rule);
  }
  .contact__list li {
    display: flex;
    align-items: center;
    gap: 4px;
    font-size: 14.5px;
    line-height: 18px;
  }
  .contact__icon { width: 13px; height: 13px; fill: var(--brand-red); flex: none; }
  .contact__address {
    font-style: normal;
    font-size: 14.5px;
    line-height: 18px;
    padding-top: 7px;
  }
</style>
</head>
<body>
  <section class="card card--front" aria-label="Business card front">
    <div class="wordmark">
      <span class="wordmark__square" aria-hidden="true"></span>
      <span class="wordmark__name">Bren Moora<br>Studio</span>
    </div>
    <div class="contact">
      <h1 class="contact__name">Maren Tollis</h1>
      <p class="contact__title">Principal</p>
      <ul class="contact__list">
        <li>
          <svg class="contact__icon" viewBox="0 0 16 16" aria-hidden="true"><path d="M2 5c0-2 3-3 6-3s6 1 6 3v1h-3V5H5v1H2zM4 7h8l2 4v3H2v-3zm4 1.5a2 2 0 100 4 2 2 0 000-4z"/></svg>
          555.014.2290 x1
        </li>
        <li>
          <svg class="contact__icon" viewBox="0 0 16 16" aria-hidden="true"><path d="M1 3h14v10H1zM2 4.2v.6l6 4 6-4v-.6L8 8z"/></svg>
          maren@brenmoorastudio.example
        </li>
        <li>
          <svg class="contact__icon" viewBox="0 0 16 16" aria-hidden="true"><circle cx="8" cy="8" r="7"/><path d="M4 6c1-1 3 0 3 1s-2 1-1 3 1 3 0 3M10 3c0 2 2 2 3 3" stroke="#fff" stroke-width="1.2" fill="none"/></svg>
          www.brenmoorastudio.example
        </li>
      </ul>
      <address class="contact__address">
        212 Alder Crossing Way,<br>
        Suite 140 Larkfield<br>
        Oregon 97401 USA
      </address>
    </div>
  </section>

  <section class="card card--back" aria-label="Business card back">
    <div class="wordmark">
      <span class="wordmark__square" aria-hidden="true"></span>
      <span class="wordmark__name">Bren Moora<br>Studio</span>
    </div>
  </section>
</body>
</html>
```